a mobile app for beauty salon professional to publish their service and customers to book service

I plan to create an iPhone app (support iPhone 6 and above) that will allow beauty salon professionals (e.g. hair stylist) to publish their service/business with address/geolocation and available time slots, manage their professional profile with photos, and service charges, allow the customers to search services based on locations, and book the service. customer can provide feedback/ratings on the professional's service. a reference website : http://velmo.trimbook.example/booking/

Target Market(s)

beauty and hair salon professionals and customers

Industry/Entity Type

Hair And Beauty

Font styles to use
Sans Serif
Script

Colors

Designer to choose colors to be used in the design.

Requirements
Must have
• === customer features
• - user/customer registration
• - customer browse nearby service using a map view
• - customer browse nearby service using a list view ordered by distance (e.g. km)
• - customer search salon service based on service category, price range, and profressional's rating
• - customer select a service with zoom in details : salon name, service offered, location/address, and a "booking" button
• - customer place booking by specifying service (e.g. simple cut, blow-dry, etc) required, time slot, preferred professional
• - customer payments (paypal/credit card)
• - customer can feedback/rate on the salon professional
• === salon professional features
• - user/professional registration
• - maintain professional profile (private/public), option to upload photos
• - a registered professional can register/maintain shop/business who by default is the owner of the shop/business
• - a shop owner can assign professionals to the shop/business (multiple professional can work in the same location/shop)
• - professional maintain their service and schedule (breaks, holidays, working hours, appointments, service rates)

```html
<!DOCTYPE html>
<html lang="en">
<head>
<meta charset="utf-8">
<title>Beauty Salon – App Design</title>
<link href="https://fonts.googleapis.com/css2?family=Montserrat:wght@500;700&family=Roboto:wght@400;500&display=swap" rel="stylesheet">
<style>
:root{
  --bg:#1f2024;
  --pink:#e8508c;
  --pink-soft:#f7c6d8;
  --ink:#222;
  --muted:#8c8c8c;
  --line:#e6e6e6;
  --white:#fff;
  --subtitle:#d9d9d9;
}
*{margin:0;padding:0;box-sizing:border-box}
html,body{width:1200px;height:983px;overflow:hidden;background:var(--bg)}
body{position:relative;font-family:Roboto,Arial,sans-serif;color:var(--ink)}
.hero-title{position:absolute;left:0;width:1200px;top:70px;text-align:center;font-family:Montserrat,sans-serif;font-weight:700;font-size:60px;color:var(--pink);letter-spacing:-.5px}
.hero-sub{position:absolute;left:0;width:1200px;top:152px;text-align:center;font-family:Montserrat,sans-serif;font-weight:500;font-size:38px;color:var(--subtitle)}
.decor{position:absolute;left:0;top:0}
.screen{position:absolute;top:290px;width:266px;height:472px;background:var(--white);border-radius:3px;overflow:hidden}
.s1{left:41px}.s2{left:324px}.s3{left:608px}.s4{left:891px}
.appbar{position:absolute;left:0;top:0;width:100%;height:45px;background:var(--pink);color:var(--white)}
.status{position:absolute;top:2px;left:5px;right:5px;font-size:8px;display:flex;justify-content:space-between}
.appbar-title{position:absolute;top:21px;width:100%;text-align:center;font-size:12.5px;font-weight:500}
.back{position:absolute;left:10px;top:22px}
.section-title{position:absolute;left:10px;top:54px;font-size:16px}
.step{position:absolute;right:10px;top:58px;font-size:10px;color:#444;letter-spacing:.2px}
.stepper{position:absolute;left:0;top:79px}
.label{position:absolute;left:10px;font-size:9px;color:#444;letter-spacing:.2px}
.field{position:absolute;left:10px;width:245px;height:36px;border:1px solid #eee;box-shadow:0 1px 3px rgba(0,0,0,.08);font-size:12px;padding-left:10px;display:flex;align-items:center}
.field svg{position:absolute;right:10px}
.avatar{position:absolute;right:24px;width:24px;height:24px;border-radius:50%;background:linear-gradient(135deg,#5b5f66,#2c2f33)}
.nav-next,.nav-back{position:absolute;top:432px;display:flex;align-items:center;font-size:11px;color:var(--pink);letter-spacing:.3px;gap:10px}
.nav-next{right:11px}.nav-back{left:11px}
.round{width:28px;height:28px;border-radius:50%;background:var(--pink);display:flex;align-items:center;justify-content:center}
.month{position:absolute;top:122px;width:100%;text-align:center;font-size:12px;color:#222}
.days{position:absolute;left:0;top:147px;width:100%}
.day{position:absolute;width:30px;margin-left:-15px;text-align:center}
.day small{display:block;font-size:7.5px;color:#555}
.day b{display:block;font-weight:400;font-size:12.5px;color:#444;margin-top:7px;height:22px;line-height:22px}
.day.on small{color:var(--pink)}
.day.on b{background:var(--pink);color:var(--white);border-radius:50%;width:24px;margin:5px auto 0;line-height:24px;height:24px;font-weight:500}
.divider{position:absolute;left:0;width:100%;top:193px;border-top:1px solid var(--line)}
.slots{position:absolute;left:7px;top:204px;display:grid;grid-template-columns:repeat(4,57px);gap:11px 8px}
.slot{height:24px;border:1px solid #eee;border-radius:3px;box-shadow:0 1px 2px rgba(0,0,0,.06);display:flex;align-items:center;justify-content:center;font-size:11.5px;color:var(--pink)}
.slot.on{background:var(--pink);color:var(--white);border-color:var(--pink)}
.card{position:absolute;left:10px;top:154px;width:245px;box-shadow:0 1px 3px rgba(0,0,0,.1)}
.row{height:32px;display:flex;align-items:center;font-size:10.5px;color:var(--muted);border-bottom:1px solid var(--line);margin-left:10px;padding-left:0}
.row:last-child{border-bottom:0}
.row svg{margin-right:10px;flex:none}
.notes{position:absolute;left:20px;top:306px;display:flex;align-items:center;font-size:10.5px;color:var(--muted)}
.notes svg{margin-right:10px}
.success-badge{position:absolute;left:76px;top:144px}
.success-title{position:absolute;top:280px;width:100%;text-align:center;font-size:15px;font-weight:500}
.success-text{position:absolute;top:310px;width:100%;text-align:center;font-size:11.5px;line-height:14.5px;color:#333}
.success-thanks{position:absolute;top:356px;width:100%;text-align:center;font-size:11.5px;color:#333}
.done-btn{position:absolute;left:11px;top:429px;width:244px;height:32px;border-radius:16px;background:var(--pink);color:var(--white);font-size:12.5px;font-weight:500;display:flex;align-items:center;justify-content:center}
</style>
</head>
<body>

<svg class="decor" width="1200" height="260" aria-hidden="true">
  <path d="M457 36v12M451 42h12" stroke="#e8508c" stroke-width="4"/>
  <circle cx="312" cy="82" r="9" fill="none" stroke="#b92be0" stroke-width="4"/>
  <path d="M919 97v14M912 104h14" stroke="#27c9c9" stroke-width="4"/>
  <circle cx="791" cy="174" r="9.5" fill="none" stroke="#e8345a" stroke-width="4"/>
  <circle cx="947" cy="164" r="7.5" fill="none" stroke="#f4c315" stroke-width="4"/>
  <circle cx="410" cy="198" r="7.5" fill="none" stroke="#f4c315" stroke-width="4"/>
  <path d="M892 190v12M886 196h12" stroke="#2f7de8" stroke-width="3.5"/>
</svg>

<h1 class="hero-title">Beauty Salon</h1>
<div class="hero-sub">App Design</div>

<!-- Reusable symbols -->
<svg width="0" height="0" style="position:absolute" aria-hidden="true">
  <defs>
    <symbol id="ico-flower" viewBox="0 0 20 20"><g fill="none" stroke="currentColor" stroke-width="1.1"><circle cx="10" cy="7" r="2"/><circle cx="10" cy="3.5" r="1.8"/><circle cx="13.3" cy="6" r="1.8"/><circle cx="6.7" cy="6" r="1.8"/><circle cx="12" cy="9.6" r="1.8"/><circle cx="8" cy="9.6" r="1.8"/><path d="M3 14c3-2 5-1 7 0h4M2 17h5c3 0 6-1 9-3"/></g></symbol>
    <symbol id="ico-clock" viewBox="0 0 20 20"><g fill="none" stroke="currentColor" stroke-width="1.3"><circle cx="10" cy="10" r="8"/><path d="M10 5v5h-4"/></g></symbol>
    <symbol id="ico-info" viewBox="0 0 20 20"><g fill="currentColor"><circle cx="10" cy="4.5" r="1.3"/><path d="M8.5 8h2.5v8h1.5v1.2h-5V16h1.5V9.2H8.5z"/></g></symbol>
    <symbol id="ico-tick" viewBox="0 0 20 20"><path d="M3 11l5 5L18 4" fill="none" stroke="currentColor" stroke-width="1.5" stroke-linecap="round" stroke-linejoin="round"/></symbol>
    <symbol id="ico-arrow" viewBox="0 0 20 20"><path d="M4 10h12M11 5l5 5-5 5" fill="none" stroke="#fff" stroke-width="1.8" stroke-linecap="round" stroke-linejoin="round"/></symbol>
    <symbol id="ico-chev" viewBox="0 0 10 10"><path d="M2 3.5l3 3 3-3" fill="none" stroke="#e8508c" stroke-width="1.2"/></symbol>
    <symbol id="ico-user" viewBox="0 0 20 20"><g fill="none" stroke="#666" stroke-width="1.2"><circle cx="10" cy="6.5" r="4"/><path d="M2.5 18c0-4 3.5-6.5 7.5-6.5s7.5 2.5 7.5 6.5z"/></g></symbol>
    <symbol id="ico-mail" viewBox="0 0 20 20"><g fill="none" stroke="#666" stroke-width="1.2"><rect x="2" y="4.5" width="16" height="11"/><path d="M2 4.5l8 6 8-6"/></g></symbol>
    <symbol id="ico-phone" viewBox="0 0 20 20"><path d="M5 2.5l3 3.5-1.8 2.2c1 2.2 2.8 4 5 5l2.2-1.8 3.5 3L15 17.5C9 17 3 11 2.5 5z" fill="none" stroke="#666" stroke-width="1.2" stroke-linejoin="round"/></symbol>
    <symbol id="ico-note" viewBox="0 0 20 20"><g fill="none" stroke="#666" stroke-width="1.2"><rect x="2.5" y="5" width="12" height="12"/><path d="M5 9h7M5 12h7M5 15h4M14.5 5V2.5H17V17h-2.5"/></g></symbol>
    <symbol id="ico-cal" viewBox="0 0 20 20"><g fill="none" stroke="#e8508c" stroke-width="1"><rect x="2" y="3.5" width="16" height="14" rx="1"/><path d="M2 7h16M6 2v3M14 2v3"/><path d="M5 10h2M9 10h2M13 10h2M5 13h2M9 13h2M13 13h2" stroke-width="1.3"/></g></symbol>
  </defs>
</svg>

<!-- Screen 1: Services -->
<section class="screen s1">
  <header class="appbar">
    <div class="status"><span>▮▮▮ Nova</span><span>9:41 AM</span><span>100% ▬</span></div>
    <svg class="back" width="10" height="14" viewBox="0 0 10 14"><path d="M8 1L2 7l6 6" fill="none" stroke="#fff" stroke-width="1.5"/></svg>
    <div class="appbar-title">Booking</div>
  </header>
  <h2 class="section-title">Services</h2>
  <div class="step">STEP 1 OF 4</div>
  <svg class="stepper" width="266" height="32">
    <g stroke="#e8508c" stroke-width="1"><path d="M52 16h32M115 16h32M181 16h32"/></g>
    <circle cx="41" cy="16" r="14" fill="#e8508c"/>
    <use href="#ico-flower" x="32" y="7" width="18" height="18" color="#fff"/>
    <use href="#ico-clock" x="91" y="9" width="15" height="15" color="#e8508c"/>
    <use href="#ico-info" x="158" y="8" width="16" height="16" color="#e8508c"/>
    <use href="#ico-tick" x="223" y="8" width="16" height="16" color="#e8508c"/>
  </svg>
  <div class="label" style="top:135px">SELECT SERVICE</div>
  <div class="field" style="top:154px">Blowdry &amp; Style<svg width="10" height="10"><use href="#ico-chev"/></svg></div>
  <div class="label" style="top:213px">ON OR AFTER</div>
  <div class="field" style="top:231px">13 March 2018<svg width="16" height="16"><use href="#ico-cal"/></svg></div>
  <div class="label" style="top:290px">WITH</div>
  <div class="field" style="top:310px">Daniel Reyes<span class="avatar" role="img" aria-label="Stylist profile photo"></span><svg width="10" height="10"><use href="#ico-chev"/></svg></div>
  <div class="nav-next">NEXT<span class="round"><svg width="14" height="14"><use href="#ico-arrow"/></svg></span></div>
</section>

<!-- Screen 2: Time -->
<section class="screen s2">
  <header class="appbar">
    <div class="status"><span>▮▮▮ Nova</span><span>9:41 AM</span><span>100% ▬</span></div>
    <svg class="back" width="10" height="14" viewBox="0 0 10 14"><path d="M8 1L2 7l6 6" fill="none" stroke="#fff" stroke-width="1.5"/></svg>
    <div class="appbar-title">Booking</div>
  </header>
  <h2 class="section-title">Time</h2>
  <div class="step">STEP 2 OF 4</div>
  <svg class="stepper" width="266" height="32">
    <g stroke="#e8508c" stroke-width="1"><path d="M51 16h32M117 16h32M181 16h32"/></g>
    <use href="#ico-flower" x="24" y="7" width="18" height="18" color="#e8508c"/>
    <circle cx="100" cy="16" r="14" fill="#e8508c"/>
    <use href="#ico-clock" x="92" y="8" width="16" height="16" color="#fff"/>
    <use href="#ico-info" x="158" y="8" width="16" height="16" color="#e8508c"/>
    <use href="#ico-tick" x="223" y="8" width="16" height="16" color="#e8508c"/>
  </svg>
  <div class="month">March 2018</div>
  <div class="days">
    <div class="day" style="left:24px"><small>Tue</small><b>13</b></div>
    <div class="day" style="left:60px"><small>Wed</small><b>14</b></div>
    <div class="day" style="left:96px"><small>Thu</small><b>15</b></div>
    <div class="day on" style="left:132px"><small>Fri</small><b>16</b></div>
    <div class="day" style="left:168px"><small>Sat</small><b>17</b></div>
    <div class="day" style="left:204px"><small>Sun</small><b>18</b></div>
    <div class="day" style="left:240px"><small>Mon</small><b>19</b></div>
  </div>
  <div class="divider"></div>
  <div class="slots">
    <div class="slot">8:00</div><div class="slot">8:30</div><div class="slot">9:00</div><div class="slot">9:30</div>
    <div class="slot">10:00</div><div class="slot">10:30</div><div class="slot">11:00</div><div class="slot">13:00</div>
    <div class="slot">13:30</div><div class="slot on">14:00</div><div class="slot">14:30</div><div class="slot">15:00</div>
    <div class="slot">15:30</div><div class="slot">16:00</div><div class="slot">16:30</div>
  </div>
  <div class="nav-back"><span class="round"><svg width="14" height="14" style="transform:scaleX(-1)"><use href="#ico-arrow"/></svg></span>BACK</div>
  <div class="nav-next">NEXT<span class="round"><svg width="14" height="14"><use href="#ico-arrow"/></svg></span></div>
</section>

<!-- Screen 3: Details -->
<section class="screen s3">
  <header class="appbar">
    <div class="status"><span>▮▮▮ Nova</span><span>9:41 AM</span><span>100% ▬</span></div>
    <svg class="back" width="10" height="14" viewBox="0 0 10 14"><path d="M8 1L2 7l6 6" fill="none" stroke="#fff" stroke-width="1.5"/></svg>
    <div class="appbar-title">Booking</div>
  </header>
  <h2 class="section-title">Details</h2>
  <div class="step">STEP 3 OF 4</div>
  <svg class="stepper" width="266" height="32">
    <g stroke="#e8508c" stroke-width="1"><path d="M51 16h32M117 16h32M183 16h32"/></g>
    <use href="#ico-flower" x="24" y="7" width="18" height="18" color="#e8508c"/>
    <use href="#ico-clock" x="92" y="9" width="15" height="15" color="#e8508c"/>
    <circle cx="166" cy="16" r="14" fill="#e8508c"/>
    <use href="#ico-info" x="158" y="8" width="16" height="16" color="#fff"/>
    <use href="#ico-tick" x="223" y="8" width="16" height="16" color="#e8508c"/>
  </svg>
  <div class="label" style="top:135px">ACCOUNT</div>
  <div class="card">
    <div class="row"><svg width="16" height="16"><use href="#ico-user"/></svg>First name</div>
    <div class="row"><svg width="16" height="16"><use href="#ico-user"/></svg>Last name</div>
    <div class="row"><svg width="16" height="16"><use href="#ico-mail"/></svg>Email address</div>
    <div class="row"><svg width="16" height="16"><use href="#ico-phone"/></svg>Phone number</div>
  </div>
  <div class="notes"><svg width="16" height="16"><use href="#ico-note"/></svg>Add Notes</div>
  <div class="nav-back"><span class="round"><svg width="14" height="14" style="transform:scaleX(-1)"><use href="#ico-arrow"/></svg></span>BACK</div>
  <div class="nav-next">NEXT<span class="round"><svg width="14" height="14"><use href="#ico-arrow"/></svg></span></div>
</section>

<!-- Screen 4: Done -->
<section class="screen s4">
  <header class="appbar">
    <div class="status"><span>▮▮▮ Nova</span><span>9:41 AM</span><span>100% ▬</span></div>
    <svg class="back" width="10" height="14" viewBox="0 0 10 14"><path d="M8 1L2 7l6 6" fill="none" stroke="#fff" stroke-width="1.5"/></svg>
    <div class="appbar-title">Booking</div>
  </header>
  <h2 class="section-title">Done</h2>
  <div class="step">STEP 4 OF 4</div>
  <svg class="stepper" width="266" height="32">
    <g stroke="#e8508c" stroke-width="1"><path d="M51 16h32M117 16h32M183 16h32"/></g>
    <use href="#ico-flower" x="24" y="7" width="18" height="18" color="#e8508c"/>
    <use href="#ico-clock" x="92" y="9" width="15" height="15" color="#e8508c"/>
    <use href="#ico-info" x="158" y="8" width="16" height="16" color="#e8508c"/>
    <circle cx="232" cy="16" r="14" fill="#e8508c"/>
    <use href="#ico-tick" x="224" y="8" width="16" height="16" color="#fff"/>
  </svg>
  <svg class="success-badge" width="114" height="114" viewBox="0 0 114 114">
    <defs>
      <radialGradient id="halo" cx="50%" cy="50%" r="50%"><stop offset="70%" stop-color="#fbd3df"/><stop offset="100%" stop-color="#fde9ee"/></radialGradient>
      <linearGradient id="core" x1="0" y1="0" x2="0" y2="1"><stop offset="0" stop-color="#f37a4f"/><stop offset="1" stop-color="#e8307f"/></linearGradient>
    </defs>
    <circle cx="57" cy="57" r="57" fill="url(#halo)"/>
    <circle cx="57" cy="57" r="45" fill="#f7a7c0"/>
    <circle cx="57" cy="57" r="36" fill="url(#core)"/>
    <g fill="none" stroke="#fff" stroke-width="2"><rect x="42" y="42" width="30" height="28" rx="3"/><path d="M42 49h30M48 39v5M66 39v5"/><path d="M47 55h4M55 55h4M63 55h4M47 62h4M55 62h4"/><path d="M63 62l2 2 4-4"/></g>
  </svg>
  <div class="success-title">Booking Successful</div>
  <div class="success-text">Your booking has been<br>successfully received.</div>
  <div class="success-thanks">Thank you!</div>
  <div class="done-btn">Done</div>
</section>

</body>
</html>
```